IT Company Business Card design

Brisk Node is a new computer solutions business focusing on setting up servers and computer systems for small to medium sized businesses.

A business client will either request a solution, or support for a current system and we will turn up on site to provide these services.

We are bast in Christchurch, New Zealand.

We are looking for unique business card's that stand out and show off the business in a professional light.

Open to all idea's etc.

Industry/Entity Type

Computer

Requirements
Must have
• Business Logo (AI file attached)
Employee Name
Business title
Business landline number
Cell phone number
Email
Web URL
Nice to have
• Could be nice to have some keywords (possibly on the back) such as:

Business IT solutions
Network installations
Phone solutions
Server management
Software diagnostics

The above is not needed, just an idea.

```html
<!DOCTYPE html>
<html lang="en">
<head>
<meta charset="utf-8">
<title>Brisk Node – Business Card</title>
<link href="https://fonts.googleapis.com/css2?family=Jost:wght@400&family=Tinos:wght@400;700&display=swap" rel="stylesheet">
<style>
  :root {
    --backdrop: #d9d9d9;
    --blue-deep: #0a4fa0;
    --blue-mid: #0b6fc4;
    --blue-bright: #12aef0;
    --card-light: #f4f4f4;
    --card-shade: #dcdcdc;
    --ink: #1a1a1a;
    --ink-soft: #333333;
    --white: #ffffff;
  }
  html, body {
    margin: 0;
    width: 1200px;
    height: 901px;
    overflow: hidden;
    background: var(--backdrop);
  }
  .canvas {
    position: relative;
    width: 1200px;
    height: 901px;
  }
  .card {
    position: absolute;
    left: 250px;
    width: 700px;
    height: 400px;
    border-radius: 26px;
    overflow: hidden;
    box-shadow: 0 6px 18px rgba(0,0,0,0.25);
  }
  .card-back {
    top: 30px;
    background: radial-gradient(ellipse at 50% 45%, var(--blue-bright) 0%, var(--blue-mid) 45%, var(--blue-deep) 100%);
    display: flex;
    flex-direction: column;
    align-items: center;
    justify-content: center;
    gap: 18px;
  }
  .back-brand {
    display: flex;
    align-items: center;
    gap: 16px;
    font-family: "Jost", sans-serif;
    font-size: 40px;
    letter-spacing: 6px;
    color: var(--white);
    text-transform: uppercase;
  }
  .back-brand .dot {
    width: 34px;
    height: 34px;
    border-radius: 50%;
    background: var(--white);
  }
  .back-url {
    font-family: "Tinos", serif;
    font-size: 22px;
    letter-spacing: 2px;
    color: var(--white);
  }
  .card-front {
    top: 470px;
    background: linear-gradient(120deg, var(--card-light) 0%, var(--white) 45%, var(--card-shade) 100%);
  }
  .base-band {
    position: absolute;
    left: 0;
    bottom: 0;
    width: 700px;
    height: 62px;
    background: linear-gradient(90deg, var(--blue-deep) 0%, var(--blue-mid) 60%, var(--blue-bright) 100%);
  }
  .base-rule {
    position: absolute;
    left: 0;
    bottom: 72px;
    width: 700px;
    height: 6px;
    background: var(--ink);
  }
  .brand {
    position: absolute;
    left: 40px;
    top: 110px;
    display: flex;
    align-items: center;
    gap: 18px;
    font-family: "Jost", sans-serif;
    font-size: 40px;
    letter-spacing: 6px;
    color: var(--ink);
    text-transform: uppercase;
  }
  .brand .dot {
    width: 52px;
    height: 52px;
    border-radius: 50%;
    background: var(--blue-mid);
  }
  .contact {
    position: absolute;
    left: 440px;
    top: 46px;
    font-family: "Tinos", serif;
    color: var(--ink-soft);
    font-size: 19px;
    line-height: 1.2;
  }
  .contact .name {
    font-weight: 700;
    font-size: 21px;
    color: var(--ink);
  }
  .contact .role { margin-bottom: 10px; }
  .contact .address { margin-bottom: 6px; }
  .contact .line {
    display: flex;
    align-items: center;
    gap: 7px;
  }
  .contact .line svg {
    width: 14px;
    height: 14px;
    flex: none;
    fill: var(--blue-mid);
  }
</style>
</head>
<body>
<div class="canvas">

  <section class="card card-back" aria-label="Card back">
    <div class="back-brand"><span class="dot"></span>Brisk Node</div>
    <div class="back-url">www.brisknode.co.nz</div>
  </section>

  <section class="card card-front" aria-label="Card front">
    <div class="base-rule"></div>
    <div class="base-band"></div>

    <div class="brand"><span class="dot"></span>Brisk Node</div>

    <div class="contact">
      <div class="name">Sample Name</div>
      <div class="role">S.E.O</div>
      <div class="address">14 Harbour Lane,<br>Riverton.</div>
      <div class="line">
        <svg viewBox="0 0 16 16"><path d="M3 1 L6 1 L7 5 L5 6.5 C6 9 7.5 10.5 10 11.5 L11.5 9.5 L15 10.5 L15 13.5 C15 14.5 14 15 13 15 C6.5 14.5 1.5 9.5 1 3 C1 2 1.8 1 3 1 Z"/></svg>
        <span>(111) 111-111</span>
      </div>
      <div class="line">
        <svg viewBox="0 0 16 16"><path d="M4 0 H12 A1.5 1.5 0 0 1 13.5 1.5 V14.5 A1.5 1.5 0 0 1 12 16 H4 A1.5 1.5 0 0 1 2.5 14.5 V1.5 A1.5 1.5 0 0 1 4 0 Z M4.5 2 V12 H11.5 V2 Z"/></svg>
        <span>(111) 111-111</span>
      </div>
      <div class="line">
        <svg viewBox="0 0 16 16"><path d="M0 3 H16 V13 H0 Z M1.5 4.2 L8 9 L14.5 4.2 Z"/></svg>
        <span>sample@brisknode.co.nz</span>
      </div>
      <div class="line">
        <svg viewBox="0 0 16 16"><path d="M8 0 A8 8 0 1 0 8.01 0 Z M8 1.5 A6.5 6.5 0 1 1 7.99 1.5 Z M7.3 1.5 H8.7 V14.5 H7.3 Z M1.5 7.3 H14.5 V8.7 H1.5 Z"/></svg>
        <span>www.brisknode.co.nz</span>
      </div>
    </div>
  </section>

</div>
</body>
</html>
```